Create a website layout for DIALMERIT.IO

****I want a website design layout mock-up not a logo - I repeat I do not any a logo*****

***This website is for a COLD CALLING COMPANY*****
***We are looking for clients the need cold callers to do the calling for them******

I am looking for a website mockup for DIALMERIT.IO. This will be a cold calling and lead generation website for real estate investors.

Please let me know if you have any questions.

```html
<!DOCTYPE html>
<html lang="en">
<head>
<meta charset="utf-8">
<title>DIALMERIT.IO — Cold Calling &amp; Lead Generation for Real Estate Investors</title>
<link rel="stylesheet" href="https://fonts.googleapis.com/css2?family=Roboto:wght@400;500;700&family=Cabin:wght@400;500;600&display=swap">
<style>
:root{
  --green:#4caf3a;
  --green-bright:#5cc149;
  --ink:#333333;
  --ink-soft:#555555;
  --dark:#3b3b3b;
  --gray-bg:#efefef;
  --card:#fafafa;
  --line:#e2e2e2;
  --white:#ffffff;
}
*{box-sizing:border-box;margin:0;padding:0}
html,body{width:1200px;height:3744px;overflow:hidden}
body{position:relative;font-family:"Roboto",Arial,sans-serif;color:var(--ink);background:var(--white)}
.abs{position:absolute}
.section-title{position:absolute;left:0;width:1200px;text-align:center;font-size:33px;font-weight:500;color:var(--ink)}

/* header */
.topbar{left:0;top:0;width:1200px;height:87px;background:var(--dark)}
.brand{left:0;top:0;width:278px;height:87px;background:var(--green);clip-path:polygon(0 0,100% 0,74% 100%,0 100%)}
.brand-name{left:20px;top:26px;color:var(--white);font-size:30px;font-weight:400;letter-spacing:.5px}
.top-social{left:937px;top:4px;display:flex;gap:4px}
.dot-icon{width:19px;height:19px;border-radius:50%;background:var(--white)}
.nav{top:42px;color:var(--white);font-size:20px}
.nav-divider{left:927px;top:34px;width:2px;height:44px;background:var(--white)}
.btn-login{left:987px;top:38px;width:161px;height:35px;border-radius:4px;background:var(--green-bright);color:var(--white);font-size:17px;display:flex;align-items:center;justify-content:center}

/* hero */
.hero{left:0;top:87px;width:1200px;height:488px;background:linear-gradient(180deg,#2e3340 0%,#4a4a52 35%,#5c4a3a 65%,#3a4a30 100%)}
.hero-title{left:0;top:185px;width:1230px;text-align:center;color:var(--white);font-size:50px;font-weight:700}
.search{left:241px;top:293px;width:720px;height:62px;background:#d8d8d8;border-radius:3px}
.field{top:310px;height:29px;background:var(--white);border-radius:3px;font-size:10px;color:var(--ink-soft);display:flex;align-items:center;padding:0 12px;justify-content:space-between}
.btn-search{left:759px;top:310px;width:121px;height:29px;background:var(--green);border-radius:3px;color:var(--white);font-size:10px;display:flex;align-items:center;justify-content:center}
.looking{left:0;top:443px;width:1166px;text-align:center;color:var(--white);font-size:16px;font-weight:500}
.chip{top:481px;height:36px;background:var(--white);border-radius:3px;font-size:11px;display:flex;align-items:center;gap:7px;padding-left:10px;color:var(--ink)}
.chip svg{width:16px;height:16px;flex:none}

/* featured */
.featured{left:0;top:575px;width:1200px;height:645px;background:var(--gray-bg)}
.pack-card{top:746px;width:298px;height:387px;background:var(--card);border:1px solid var(--line);border-radius:6px}
.pack-photo{position:absolute;left:8px;top:8px;width:280px;height:188px;background:linear-gradient(160deg,#c9ccd0,#8d9096 60%,#4e5055)}
.price{position:absolute;left:8px;top:170px;width:140px;height:26px;background:var(--green);clip-path:polygon(0 0,88% 0,100% 100%,0 100%);color:var(--white);font-size:13px;font-weight:500;padding:5px 0 0 12px}
.pack-type{position:absolute;left:22px;top:210px;color:var(--green);font-size:15px;font-weight:500}
.pack-market{position:absolute;left:22px;top:242px;font-size:11px;color:var(--ink-soft);display:flex;gap:12px;align-items:center;white-space:nowrap}
.pack-meta{position:absolute;left:28px;top:277px;font-size:9px;color:var(--ink-soft);display:flex;gap:34px}
.pack-foot{position:absolute;left:0;top:322px;width:296px;border-top:2px solid var(--line);height:63px}
.avatar{position:absolute;left:22px;top:13px;width:44px;height:44px;border-radius:50%;background:#5a5d66}
.user{position:absolute;left:76px;top:28px;font-size:10px;font-weight:500}
.ago{position:absolute;right:24px;top:28px;font-size:10px;font-style:italic;font-weight:500}
.dots{left:0;width:1214px;display:flex;justify-content:center;gap:3px}
.dots span{width:11px;height:11px;border-radius:50%;background:var(--ink)}
.dots span:first-child{background:var(--white)}

/* markets */
.city{top:1406px;width:304px;height:188px;border-radius:4px;color:var(--white);font-size:15px;font-weight:500;display:flex;align-items:flex-end;justify-content:center;padding-bottom:16px}

/* why */
.why{left:0;top:1705px;width:1200px;height:580px;background:var(--gray-bg)}
.why-card{top:1858px;width:298px;height:387px;background:var(--card);border:1px solid var(--line);border-radius:4px;text-align:center}
.why-icon{position:absolute;left:94px;top:53px;width:112px;height:112px;border-radius:50%;background:var(--green-bright)}
.why-icon svg{width:112px;height:112px}
.why-title{position:absolute;left:0;top:212px;width:100%;font-size:21px;font-weight:500;color:var(--ink)}
.why-text{position:absolute;left:42px;top:258px;width:214px;font-size:11px;line-height:15px;color:var(--ink-soft)}

/* testimonial */
.face{top:2439px;width:137px;height:137px;border-radius:50%}
.t-name{left:0;top:2622px;width:1258px;text-align:center;font-family:"Cabin",sans-serif;font-size:25px;font-weight:600}
.t-role{left:0;top:2658px;width:1258px;text-align:center;font-family:"Cabin",sans-serif;font-size:19px;color:var(--green)}
.t-text{left:0;top:2730px;width:1258px;text-align:center;font-family:"Cabin",sans-serif;font-size:19px;line-height:25px;color:var(--ink-soft)}

/* register */
.register{left:0;top:2863px;width:1200px;height:170px;background:linear-gradient(180deg,#5cb844,#4aa33a)}
.reg-title{left:88px;top:2900px;color:var(--white);font-size:34px;font-weight:500}
.reg-sub{left:88px;top:2950px;color:var(--white);font-size:19px}
.btn-register{left:876px;top:2912px;width:234px;height:70px;border-radius:4px;background:var(--green-bright);color:var(--white);font-size:25px;display:flex;align-items:center;justify-content:center}

/* partners */
.partners-sub{left:0;top:3117px;width:1226px;text-align:center;font-size:12px;color:var(--ink-soft)}
.partner{top:3190px;height:70px;display:flex;align-items:center;gap:8px;font-size:24px;color:#8a8a8a;font-weight:500;white-space:nowrap}
.partner i{display:block;width:14px;height:14px;background:#8a8a8a}

/* footer */
.footer{left:0;top:3310px;width:1200px;height:434px;background:var(--dark)}
.f-head{top:3383px;color:var(--white);font-size:25px;font-weight:500}
.f-text{color:var(--white);font-size:11px;line-height:21px}
.f-social{left:833px;top:3420px;display:flex;gap:4px}
.f-social span{width:29px;height:29px;border-radius:50%;background:var(--white)}
.email{left:832px;top:3538px;width:206px;height:44px;border-radius:6px;background:var(--white);color:#666;font-size:14px;padding:13px 0 0 24px}
.btn-go{left:1052px;top:3541px;width:60px;height:39px;background:var(--green-bright);color:var(--white);font-size:16px;display:flex;align-items:center;justify-content:center}
.f-rule{left:70px;top:3627px;width:1056px;height:1px;background:#8a8a8a}
.copyright{left:70px;top:3677px;color:var(--white);font-size:19px}
</style>
</head>
<body>

<!-- header -->
<div class="abs topbar"></div>
<div class="abs brand"></div>
<div class="abs brand-name">DIALMERIT.IO</div>
<div class="abs top-social"><span class="dot-icon"></span><span class="dot-icon"></span><span class="dot-icon"></span><span class="dot-icon"></span><span class="dot-icon"></span><span class="dot-icon"></span></div>
<div class="abs nav" style="left:553px">Home</div>
<div class="abs nav" style="left:660px">Services <svg width="14" height="10" viewBox="0 0 14 10"><path d="M2 2l5 5 5-5" fill="none" stroke="#fff" stroke-width="2"/></svg></div>
<div class="abs nav" style="left:802px">Contact</div>
<div class="abs nav-divider"></div>
<div class="abs btn-login">Login/Register</div>

<!-- hero -->
<div class="abs hero" role="img" aria-label="Modern two-storey house with lit windows at dusk"></div>
<div class="abs hero-title">We dial your next great deal</div>
<div class="abs search"></div>
<div class="abs field" style="left:268px;width:120px">Lead Type... <svg width="10" height="7" viewBox="0 0 10 7"><path d="M1 1l4 4 4-4" fill="none" stroke="#555" stroke-width="1.5"/></svg></div>
<div class="abs field" style="left:426px;width:120px;justify-content:flex-start;padding-left:36px">Market...</div>
<div class="abs field" style="left:582px;width:120px">Volume... <svg width="10" height="7" viewBox="0 0 10 7"><path d="M1 1l4 4 4-4" fill="none" stroke="#555" stroke-width="1.5"/></svg></div>
<div class="abs btn-search">Get Leads</div>
<div class="abs looking">What do you need from us?</div>
<div class="abs chip" style="left:317px;width:120px"><svg viewBox="0 0 16 16"><path d="M4 1l3 3-2 2c1 2 3 4 5 5l2-2 3 3-2 3C7 15 1 9 1 3z" fill="#333"/></svg>Cold Calling</div>
<div class="abs chip" style="left:454px;width:120px"><svg viewBox="0 0 16 16"><path d="M2 2h12v9H6l-4 3z" fill="#333"/></svg>SMS Follow-up</div>
<div class="abs chip" style="left:590px;width:106px"><svg viewBox="0 0 16 16"><path d="M2 3h2M6 3h8M2 8h2M6 8h8M2 13h2M6 13h8" stroke="#333" stroke-width="1.8"/></svg>Lead Lists</div>
<div class="abs chip" style="left:727px;width:120px"><svg viewBox="0 0 16 16"><rect x="2" y="3" width="12" height="11" fill="none" stroke="#333" stroke-width="1.5"/><path d="M2 6h12M5 1v3M11 1v3" stroke="#333" stroke-width="1.5"/></svg>Appointments</div>

<!-- featured packages -->
<div class="abs featured"></div>
<div class="section-title" style="top:668px">Featured Lead Packages</div>

<div class="abs pack-card" style="left:132px">
  <div class="pack-photo" role="img" aria-label="Call team working with headsets at desks"></div>
  <div class="price">$1,450/mo</div>
  <div class="pack-type">Motivated Sellers</div>
  <div class="pack-market"><svg width="14" height="18" viewBox="0 0 14 18"><path d="M1 1l12 6-6 2-2 8z" fill="#4caf3a"/></svg>Absentee owners, san francisco, C1293</div>
  <div class="pack-meta"><span>Calls : 4000</span><span>Hours : 80</span><span>Leads : 120</span></div>
  <div class="pack-foot"><div class="avatar" role="img" aria-label="Team lead portrait"></div><div class="user">Team Lead</div><div class="ago">Updated daily</div></div>
</div>
<div class="abs pack-card" style="left:454px">
  <div class="pack-photo" role="img" aria-label="Caller on the phone at a laptop"></div>
  <div class="price">$2,200/mo</div>
  <div class="pack-type">Probate Leads</div>
  <div class="pack-market"><svg width="14" height="18" viewBox="0 0 14 18"><path d="M1 1l12 6-6 2-2 8z" fill="#4caf3a"/></svg>Inherited homes, san francisco, C1293</div>
  <div class="pack-meta"><span>Calls : 6000</span><span>Hours : 120</span><span>Leads : 180</span></div>
  <div class="pack-foot"><div class="avatar" role="img" aria-label="Team lead portrait"></div><div class="user">Team Lead</div><div class="ago">Updated daily</div></div>
</div>
<div class="abs pack-card" style="left:774px">
  <div class="pack-photo" role="img" aria-label="Office floor with callers and monitors"></div>
  <div class="price">$3,100/mo</div>
  <div class="pack-type">Pre-Foreclosure</div>
  <div class="pack-market"><svg width="14" height="18" viewBox="0 0 14 18"><path d="M1 1l12 6-6 2-2 8z" fill="#4caf3a"/></svg>Distressed owners, san francisco, C1293</div>
  <div class="pack-meta"><span>Calls : 8000</span><span>Hours : 160</span><span>Leads : 240</span></div>
  <div class="pack-foot"><div class="avatar" role="img" aria-label="Team lead portrait"></div><div class="user">Team Lead</div><div class="ago">Updated daily</div></div>
</div>
<div class="abs dots" style="top:1185px"><span></span><span></span><span></span><span></span></div>

<!-- markets -->
<div class="section-title" style="top:1316px">We call sellers in these markets</div>
<div class="abs city" style="left:115px;background:linear-gradient(180deg,#6fa6d6,#4f86a8 45%,#5b6a45)" role="img" aria-label="Coastal city skyline with beach and green hills">Honolulu</div>
<div class="abs city" style="left:456px;background:linear-gradient(180deg,#a9b4c4,#7c8590 55%,#4d4f52)" role="img" aria-label="City skyline with glass tower">Boston</div>
<div class="abs city" style="left:797px;background:linear-gradient(180deg,#1f3a48,#2f5c68 50%,#2a3540)" role="img" aria-label="Night skyline of casino towers">las vegas</div>
<div class="abs dots" style="top:1649px;width:1236px"><span></span><span></span><span></span><span></span></div>

<!-- why -->
<div class="abs why"></div>
<div class="section-title" style="top:1764px;width:1226px">Why Choose Us?</div>

<div class="abs why-card" style="left:144px">
  <div class="why-icon"><svg viewBox="0 0 112 112"><path d="M24 58l14-16 14 4 10-4 14 2 12 14-18 18-6-6-6 6-8-8-6 4z" fill="#fff"/><path d="M52 46l10 10" stroke="#5cc149" stroke-width="3"/></svg></div>
  <div class="why-title">Trained Cold Callers</div>
  <div class="why-text">Our callers are trained on real estate scripts, handle objections with ease and qualify every seller before the lead reaches you.</div>
</div>
<div class="abs why-card" style="left:477px">
  <div class="why-icon"><svg viewBox="0 0 112 112"><path d="M46 30h20l-6 10c14 6 22 18 22 30 0 10-10 14-26 14s-26-4-26-14c0-12 8-24 22-30z" fill="#fff"/><text x="56" y="78" text-anchor="middle" font-family="Roboto,sans-serif" font-size="28" font-weight="700" fill="#5cc149">$</text></svg></div>
  <div class="why-title">More Deals, Less Cost</div>
  <div class="why-text">Skip hiring and training in-house staff. Pay one flat monthly rate and spend your time closing deals.</div>
</div>
<div class="abs why-card" style="left:810px">
  <div class="why-icon"><svg viewBox="0 0 112 112"><path d="M24 60l22-20 22 20v22H24z" fill="#fff"/><path d="M56 46l14-12 20 18v28H70" fill="none" stroke="#fff" stroke-width="4"/><rect x="40" y="62" width="10" height="10" fill="#5cc149"/></svg></div>
  <div class="why-title">Motivated Sellers Only</div>
  <div class="why-text">Every lead is screened for motivation, timeline and asking price so you only talk to sellers ready to act.</div>
</div>

<!-- testimonial -->
<div class="section-title" style="top:2352px;width:1240px">Testimonial</div>
<div class="abs face" style="left:196px;background:#c9a27e" role="img" aria-label="Client portrait"></div>
<div class="abs face" style="left:373px;background:#7d7470" role="img" aria-label="Client portrait"></div>
<div class="abs face" style="left:549px;background:#b8774a" role="img" aria-label="Client portrait"></div>
<div class="abs face" style="left:725px;background:#cfd3d8" role="img" aria-label="Client portrait"></div>
<div class="abs face" style="left:902px;background:#c9a27e" role="img" aria-label="Client portrait"></div>
<div class="abs t-name">Lena Marsh</div>
<div class="abs t-role">Real Estate Investor</div>
<div class="abs t-text">Their callers booked twelve seller appointments in our<br>first month, and we closed three deals from them.</div>

<!-- register -->
<div class="abs register" role="img" aria-label="Row of townhouses under a green tint"></div>
<div class="abs reg-title">Hire Your Cold Calling Team</div>
<div class="abs reg-sub">Start getting motivated seller leads this week</div>
<div class="abs btn-register">Get Started</div>

<!-- partners -->
<div class="section-title" style="top:3072px;width:1226px">Trusted Partners</div>
<div class="abs partners-sub">Investors and agencies who rely on our callers</div>
<div class="abs partner" style="left:158px"><i></i>Harbor Group</div>
<div class="abs partner" style="left:362px">Northgate</div>
<div class="abs partner" style="left:568px"><i></i>Linden &amp; Co</div>
<div class="abs partner" style="left:728px;font-size:20px">Crestline Estates</div>
<div class="abs partner" style="left:936px;font-size:21px">Keystone Realty</div>

<!-- footer -->
<div class="abs footer"></div>
<div class="abs f-head" style="left:86px">About Site</div>
<div class="abs f-text" style="left:38px;top:3452px;width:252px;text-align:center">Cold calling and lead generation for real estate investors. We find motivated sellers so you can close.</div>
<div class="abs f-head" style="left:367px">Quick Links</div>
<div class="abs f-text" style="left:367px;top:3450px;line-height:31.5px">About Us<br>Terms &amp; Conditions<br>User's Guide<br>Support Center<br>Press Info</div>
<div class="abs f-head" style="left:581px;top:3380px">Contact Us</div>
<div class="abs f-text" style="left:581px;top:3452px;line-height:31.5px">info@DIALMERIT.IO.com<br>xyz road, st street, C1293,<br>san francisco<br>+1 555-0142-118<br>+1 555-0142-119</div>
<div class="abs f-head" style="left:839px;top:3378px">Follow us</div>
<div class="abs f-social"><span></span><span></span><span></span><span></span><span></span><span></span></div>
<div class="abs f-head" style="left:835px;top:3486px">Subscribe</div>
<div class="abs email">email address......</div>
<div class="abs btn-go">GO</div>
<div class="abs f-rule"></div>
<div class="abs copyright">© 2020 DIALMERIT.IO. Your trusted Partner</div>

</body>
</html>
```